Uni Camp Poster (Theme: Desert Oasis)

We require a poster design for our annual camp with the theme "desert oasis", please see the attached design brief for details.
We are the Meridian Fellowship (Mf), founded in 1996 at the Collingwood Institute of Learning. As one of the largest social clubs at the Collingwood Institute of Learning, Mf runs a variety of premier social and sporting events for University students.
Target Market(s)
18-19 year olds in Melbourne

```html
<!DOCTYPE html>
<html lang="en">
<head>
<meta charset="utf-8">
<title>A Journey Through the Sands – Meridian Fellowship Camp</title>
<link rel="stylesheet" href="https://fonts.googleapis.com/css2?family=Cinzel:wght@700;900&family=Almendra:wght@700&family=Oswald:wght@400;600&display=swap">
<style>
  :root {
    --sky-deep: #1c1f4a;
    --sky-violet: #4a3a6e;
    --sky-rose: #8a6a86;
    --haze: #c9ccd8;
    --haze-blue: #8e9bc4;
    --dune-dark: #2a1c16;
    --dune-warm: #6b4a34;
    --gold-light: #fff2c4;
    --gold: #d9a43a;
    --gold-deep: #7a4a10;
    --ink: #231a0c;
    --white: #ffffff;
  }
  * { margin: 0; padding: 0; box-sizing: border-box; }
  html, body { width: 1194px; height: 1200px; overflow: hidden; }
  body { font-family: "Oswald", sans-serif; }

  .poster {
    position: relative;
    width: 1194px;
    height: 1200px;
    overflow: hidden;
  }

  .poster__scene {
    position: absolute;
    inset: 0;
    background:
      radial-gradient(ellipse 45% 22% at 50% 55%, rgba(255,255,255,0.55), transparent 70%),
      linear-gradient(180deg,
        var(--sky-deep) 0%,
        var(--sky-violet) 14%,
        var(--sky-rose) 30%,
        var(--haze) 50%,
        var(--haze) 60%,
        var(--haze-blue) 70%,
        var(--dune-warm) 86%,
        var(--dune-dark) 100%);
  }

  .club-name {
    position: absolute;
    top: 101px;
    left: 450px;
    display: flex;
    align-items: center;
    gap: 14px;
    color: var(--white);
  }
  .club-name__dot {
    width: 60px;
    height: 60px;
    border-radius: 50%;
    border: 3px solid var(--white);
  }
  .club-name__text {
    font-family: "Oswald", sans-serif;
    font-weight: 400;
    font-size: 36px;
    line-height: 40px;
    letter-spacing: 1px;
    text-transform: uppercase;
  }

  .affiliation-badge {
    position: absolute;
    top: 24px;
    left: 1068px;
    width: 100px;
    height: 74px;
    border-radius: 8px;
    background: rgba(255,255,255,0.85);
  }

  .title {
    position: absolute;
    top: 340px;
    left: 0;
    width: 100%;
    text-align: center;
  }
  .title__main {
    display: block;
    font-family: "Cinzel", serif;
    font-weight: 900;
    font-size: 176px;
    line-height: 190px;
    letter-spacing: -4px;
    color: var(--gold-light);
    background: linear-gradient(180deg, var(--white) 10%, var(--gold-light) 45%, var(--gold) 80%, var(--gold-deep) 100%);
    -webkit-background-clip: text;
    background-clip: text;
    -webkit-text-fill-color: transparent;
    filter: drop-shadow(4px 6px 0 var(--gold-deep)) drop-shadow(0 10px 12px rgba(0,0,0,0.45));
  }
  .title__sub {
    display: block;
    margin-top: -14px;
    font-family: "Almendra", serif;
    font-weight: 700;
    font-size: 62px;
    line-height: 70px;
    color: var(--gold-light);
    background: linear-gradient(180deg, var(--white) 20%, var(--gold) 90%);
    -webkit-background-clip: text;
    background-clip: text;
    -webkit-text-fill-color: transparent;
    filter: drop-shadow(3px 4px 0 var(--gold-deep)) drop-shadow(0 6px 8px rgba(0,0,0,0.4));
  }

  .divider {
    position: absolute;
    top: 625px;
    left: 529px;
    width: 140px;
    height: 4px;
    background: #4a4436;
  }

  .dates {
    position: absolute;
    top: 652px;
    left: 0;
    width: 100%;
    text-align: center;
    font-family: "Oswald", sans-serif;
    font-weight: 400;
    font-size: 82px;
    line-height: 100px;
    color: var(--ink);
    text-shadow: 0 0 2px rgba(255,220,140,0.8);
  }
  .dates sup {
    font-size: 40px;
    vertical-align: 34px;
    line-height: 0;
  }

  .price {
    position: absolute;
    top: 1102px;
    left: 183px;
    width: 831px;
    height: 66px;
    border: 2px solid var(--white);
    border-radius: 33px;
    background: rgba(20,14,10,0.25);
    display: flex;
    align-items: center;
    justify-content: center;
    font-family: "Oswald", sans-serif;
    font-weight: 600;
    font-size: 38px;
    letter-spacing: 0.5px;
    color: var(--white);
  }
</style>
</head>
<body>
  <main class="poster">
    <div class="poster__scene" role="img" aria-label="Desert landscape at dusk: stormy violet sky over hazy pyramids, a distant city, acacia trees and red rocky cliffs"></div>

    <div class="club-name">
      <span class="club-name__dot"></span>
      <span class="club-name__text">Meridian<br>Fellowship</span>
    </div>

    <div class="affiliation-badge" aria-hidden="true"></div>

    <h1 class="title">
      <span class="title__main">A JOURNEY</span>
      <span class="title__sub">Through the Sands</span>
    </h1>

    <div class="divider"></div>

    <p class="dates">11<sup>th</sup> to 13<sup>th</sup> March 2022</p>

    <p class="price">$155 for Members and $165 for Non-Members</p>
  </main>
</body>
</html>
```